Building company needs a letterhead design

I'm after a modern but professional letter head.
Must have the below details:
- Logo
- Website - TARVELGROUP.COM.AU
- Email - INFO@TARVELGROUP.COM.AU
- Office - 03 58206317
- Mobile number - 0413865290
- ABN - 47 318 264 105
...........................................................................................................................................................................................................................
- Logo
- Office - 03 58206317
- ABN - 47 318 264 105

Target Market(s)

.

Industry/Entity Type

Construction Company

Font styles to use
Sans Serif

Requirements
Must have
• Must have the below details:
• - Logo
• - Website - TARVELGROUP.COM.AU
• - Email - INFO@TARVELGROUP.COM.AU
• - Office - 03 58206317
• - Mobile number - 0413865290
• - ABN - 47 318 264 105
Nice to have
• .
Should not have
• .

```html
<!DOCTYPE html>
<html lang="en">
<head>
<meta charset="utf-8">
<title>Tarvel Building Group Letterhead</title>
<link rel="stylesheet" href="https://fonts.googleapis.com/css2?family=Open+Sans:wght@400;800&display=swap">
<style>
  :root {
    --charcoal: #1e2122;
    --amber: #f6b21a;
    --amber-pale: #fde3a2;
    --mist: #e4e4e4;
    --paper: #ffffff;
    --ink-light: #ffffff;
  }
  * { margin: 0; padding: 0; box-sizing: border-box; }
  html, body { width: 927px; height: 1200px; overflow: hidden; background: var(--paper); }
  .letterhead {
    position: relative;
    width: 927px;
    height: 1200px;
    background: var(--paper);
    font-family: "Open Sans", sans-serif;
  }
  .edge-band {
    position: absolute;
    left: 0;
    width: 927px;
    height: 6px;
    background: var(--charcoal);
  }
  .edge-band--top { top: 0; }
  .edge-band--bottom { bottom: 0; }

  .masthead {
    position: absolute;
    left: 19px;
    top: 0;
    width: 426px;
    height: 198px;
    background: var(--charcoal);
  }
  .masthead__mark {
    position: absolute;
    left: 82px;
    top: 60px;
    width: 66px;
    height: 82px;
    background: var(--amber);
  }
  .masthead__name {
    position: absolute;
    left: 166px;
    top: 70px;
    color: var(--amber);
    font-weight: 800;
    text-transform: uppercase;
    line-height: 1;
  }
  .masthead__name-main { display: block; font-size: 38px; letter-spacing: 0.5px; }
  .masthead__name-sub { display: block; font-size: 16px; letter-spacing: 2.6px; margin-top: 6px; }

  .emblem {
    position: absolute;
    left: 0;
    top: 420px;
    width: 927px;
    text-align: center;
  }
  .emblem__mark {
    width: 237px;
    height: 305px;
    margin: 0 auto;
    background: var(--mist);
  }
  .emblem__name {
    color: var(--amber-pale);
    font-weight: 800;
    text-transform: uppercase;
    line-height: 1;
  }
  .emblem__name-main { display: block; font-size: 84px; letter-spacing: 2px; margin-top: 22px; }
  .emblem__name-sub { display: block; font-size: 33px; letter-spacing: 5px; margin-top: 10px; }

  .contact-panel {
    position: absolute;
    left: 19px;
    top: 1001px;
    width: 426px;
    height: 193px;
    background: var(--charcoal);
    padding: 18px 0 0 28px;
  }
  .contact-list { list-style: none; }
  .contact-list__item {
    display: flex;
    align-items: center;
    height: 31px;
    color: var(--ink-light);
    font-size: 23px;
    font-weight: 400;
  }
  .contact-list__label {
    width: 68px;
    color: var(--amber);
  }
  .contact-list__icon {
    width: 68px;
    padding-left: 29px;
    display: flex;
    align-items: center;
  }
  .contact-list__icon svg { width: 22px; height: 22px; fill: var(--amber); }
</style>
</head>
<body>
<main class="letterhead">
  <div class="edge-band edge-band--top"></div>

  <header class="masthead">
    <div class="masthead__mark"></div>
    <h1 class="masthead__name">
      <span class="masthead__name-main">Tarvel</span>
      <span class="masthead__name-sub">Building Group</span>
    </h1>
  </header>

  <section class="emblem" aria-hidden="true">
    <div class="emblem__mark"></div>
    <p class="emblem__name">
      <span class="emblem__name-main">Tarvel</span>
      <span class="emblem__name-sub">Building Group</span>
    </p>
  </section>

  <footer class="contact-panel">
    <ul class="contact-list">
      <li class="contact-list__item">
        <span class="contact-list__label">ADN</span>
        <span>47 318 264 105</span>
      </li>
      <li class="contact-list__item">
        <span class="contact-list__icon">
          <svg viewBox="0 0 24 24" aria-label="Office phone"><path d="M3 9c0-3 4-5 9-5s9 2 9 5v2h-5V9H8v2H3z M5 13h14l1 7H4z M12 14.5a2.5 2.5 0 1 0 0 5a2.5 2.5 0 1 0 0-5z"/></svg>
        </span>
        <span>03 58206317</span>
      </li>
      <li class="contact-list__item">
        <span class="contact-list__icon">
          <svg viewBox="0 0 24 24" aria-label="Mobile"><path d="M8 2h2v3h5a2 2 0 0 1 2 2v13a2 2 0 0 1-2 2H9a2 2 0 0 1-2-2V7a2 2 0 0 1 1-1.7z M9.5 8v5h5V8z"/></svg>
        </span>
        <span>0413865290</span>
      </li>
      <li class="contact-list__item">
        <span class="contact-list__icon">
          <svg viewBox="0 0 24 24" aria-label="Email"><path d="M2 5h20v14H2z M4 7v.3l8 6 8-6V7z M4 9.8V17h16V9.8l-8 6z" fill-rule="evenodd"/></svg>
        </span>
        <span>INFO@TARVELGROUP.COM.AU</span>
      </li>
      <li class="contact-list__item">
        <span class="contact-list__icon">
          <svg viewBox="0 0 24 24" aria-label="Website"><path d="M11 2a9 9 0 1 0 0 18a9 9 0 1 0 0-18z M11 4a7 7 0 0 1 6.9 6H4.1A7 7 0 0 1 11 4z M4.1 12h13.8a7 7 0 0 1-13.8 0z M14 13l8 3-3 1 3 3-1.5 1.5-3-3-1 3z" fill-rule="evenodd"/></svg>
        </span>
        <span>TARVELGROUP.COM.AU</span>
      </li>
    </ul>
  </footer>

  <div class="edge-band edge-band--bottom"></div>
</main>
</body>
</html>
```